KELPO's Coffee Liqueur Shot Arabica

Need a lable for a 500ml bottle of homemade Coffee liqueur.
Name:
KELPO's
Coffee
Shot

Shape: Round, 80mm
Color of the lable should be black and letters in black.
Letters KELPO's min 12mm hight.
Color of the liqueur is dark brown.
Add: 500ml
Add: 38% vol.
Should have a bean on the lable.
Maybe some bullet words on the bottom...
Prefered design see Pic1a with bottle.

Target Market(s)

People that enjoy coffee in shots, in coctails, with ice or on top of icecream or any other dessert

Font styles to use
Serif

Colors

Designer to choose colors to be used in the design.

Requirements
Must have
• See Pic 1a
Nice to have
• See Pic1a (bottle)
Should not have
• Different colors

```html
<!DOCTYPE html>
<html lang="en">
<head>
<meta charset="utf-8">
<title>KELPO's Coffee Shot – Round Label</title>
<link rel="stylesheet" href="https://fonts.googleapis.com/css2?family=Alfa+Slab+One&family=Oswald:wght@500;600&display=swap">
<style>
  :root {
    --ink: #111111;
    --paper: #ffffff;
    --page: #ffffff;
    --cut-line: #b9b9b9;
  }
  html, body {
    margin: 0;
    padding: 0;
    width: 740px;
    height: 1200px;
    overflow: hidden;
    background: var(--page);
  }
  .label-canvas {
    display: block;
    width: 740px;
    height: 1200px;
  }
  .brand-name {
    font-family: "Alfa Slab One", serif;
    font-size: 66px;
    fill: var(--ink);
    letter-spacing: 2px;
  }
  .tagline {
    font-family: "Alfa Slab One", serif;
    font-size: 30px;
    fill: var(--ink);
    letter-spacing: 1px;
  }
  .premium {
    font-family: "Oswald", sans-serif;
    font-weight: 500;
    font-size: 20px;
    fill: var(--paper);
    letter-spacing: 2px;
  }
  .product-name {
    font-family: "Oswald", sans-serif;
    font-weight: 600;
    font-size: 86px;
    fill: var(--paper);
  }
  .band-text {
    font-family: "Oswald", sans-serif;
    font-weight: 500;
    font-size: 36px;
    fill: var(--paper);
  }
  .star { fill: var(--ink); }
</style>
</head>
<body>
<svg class="label-canvas" viewBox="0 0 740 1200" xmlns="http://www.w3.org/2000/svg" role="img" aria-label="KELPO's Premium Coffee Shot round label, 38% vol, 500ml, spiced coffee">
  <defs>
    <path id="arc-top" d="M 195 600 A 175 175 0 0 1 545 600"/>
    <path id="arc-bottom" d="M 165 600 A 205 205 0 0 0 575 600"/>
  </defs>

  <!-- cut line and label base -->
  <circle class="label-cut" cx="370" cy="600" r="300" fill="var(--paper)" stroke="var(--cut-line)" stroke-width="1.5"/>

  <!-- border rings -->
  <g class="label-rings" fill="none" stroke="var(--ink)">
    <circle cx="370" cy="600" r="278" stroke-width="16"/>
    <circle cx="370" cy="600" r="260" stroke-width="2.5"/>
    <circle cx="370" cy="600" r="249" stroke-width="5" stroke-dasharray="0.1 9" stroke-linecap="round"/>
    <circle cx="370" cy="600" r="238" stroke-width="2.5"/>
  </g>

  <!-- brand arc -->
  <text class="brand-name" text-anchor="middle">
    <textPath href="#arc-top" startOffset="50%">KELPO'S</textPath>
  </text>

  <!-- volume band -->
  <g class="volume-band">
    <rect x="92" y="558" width="556" height="88" rx="24" fill="var(--ink)"/>
    <rect x="100" y="566" width="540" height="72" rx="18" fill="none" stroke="var(--paper)" stroke-width="2.5"/>
    <text class="band-text" x="178" y="616" text-anchor="middle" textLength="104" lengthAdjust="spacingAndGlyphs">38% VOL</text>
    <text class="band-text" x="566" y="616" text-anchor="middle" textLength="86" lengthAdjust="spacingAndGlyphs">500ML</text>
  </g>

  <!-- centre medallion -->
  <g class="medallion">
    <circle cx="370" cy="600" r="132" fill="var(--paper)"/>
    <circle cx="370" cy="600" r="125" fill="var(--ink)"/>
    <circle cx="370" cy="600" r="116" fill="none" stroke="var(--paper)" stroke-width="2"/>
    <text class="premium" x="370" y="510" text-anchor="middle">★ PREMIUM ★</text>
    <text class="product-name" x="370" y="596" text-anchor="middle" textLength="186" lengthAdjust="spacingAndGlyphs">COFFEE</text>
    <text class="product-name" x="370" y="676" text-anchor="middle" textLength="134" lengthAdjust="spacingAndGlyphs">SHOT</text>
    <path d="M 276 626 L 290 626 L 282 664" fill="none" stroke="var(--paper)" stroke-width="2.5"/>
    <path d="M 464 626 L 450 626 L 458 664" fill="none" stroke="var(--paper)" stroke-width="2.5"/>
  </g>

  <!-- bottom tagline -->
  <text class="tagline" text-anchor="middle">
    <textPath href="#arc-bottom" startOffset="22%">SPICED</textPath>
  </text>
  <text class="tagline" text-anchor="middle">
    <textPath href="#arc-bottom" startOffset="78%">COFFEE</textPath>
  </text>
  <text class="star" x="172" y="670" font-size="20" text-anchor="middle">★</text>
  <text class="star" x="568" y="670" font-size="20" text-anchor="middle">★</text>

  <!-- coffee bean artwork area -->
  <ellipse class="bean-artwork" cx="370" cy="778" rx="58" ry="32" fill="var(--ink)" role="img" aria-label="Three coffee beans illustration"/>
</svg>
</body>
</html>
```